Flyer für Textilien mit individueller Bestickung oder Bedruckung
Wir waren mit der Designerin hochzufrieden. Alle Änderungen und Wünsche wurden schnell und sehr kompetent bearbeitet. Sind von dem Ergebnis begeistert.
Zielgruppe
Vertrieb von Logobekleidung, wie z.B. Strickwaren, Polo Shirts und T Shirts.
Zielgruppe sind Golfclubs, Proshops, Vereine, Schulen (Schulbekleidung ), Arztpraxen sowie alle Firmen und Institutionen, die Bekleidung mit individueller Bestickung oder Bedruckung benötigen.
Aufgabenstellung
Es soll ein Flyer erstellt werden, der nicht überfrachtet ist und dem Kunden schnelle und transparente Informationen liefert. Es sollen sich möglichst viele Branchen angesprochen fühlen. Auf den grünen Button mit "golf" sollte daher verzichtet werden.
Auf unserer Internetseite www.velmax.de wird deutlich, das es zwei Geschäftsfelder in unserer Firma gibt, Golfshop einerseits und Werbetextilien andererseits. Der gewünschte Flyer soll das Thema Werbetextilien abdecken. Im Datenanhang haben wir einen von uns erstellten Flyer angehängt, der lediglich als Anhaltspunkt gelten soll. Wir begrüssen es sehr wenn der Designer sich von der Vorlage löst. Unser Logo 'velmax artline' steht für das Werbetextil Geschäft und ist gleichzeitig unsere Marke, unter der wir unsere Strickwaren produzieren.
Die Sprache sollte Deutsch sein.

```html
<!DOCTYPE html>
<html lang="de">
<head>
<meta charset="utf-8">
<title>velmax artline – Flyer</title>
<link href="https://fonts.googleapis.com/css2?family=Michroma&family=Roboto:wght@300;400;700&display=swap" rel="stylesheet">
<style>
  :root{
    --bg:#b9b9b9;
    --paper:#ffffff;
    --paper-fade:#cfd0d2;
    --green:#8cc01f;
    --green-light:#b2d65a;
    --green-text:#7fb51a;
    --ink:#3a3a3a;
    --ink-soft:#555;
    --red:#e30613;
    --white:#ffffff;
  }
  *{box-sizing:border-box;margin:0;padding:0}
  html,body{width:913px;height:1200px;overflow:hidden}
  body{background:linear-gradient(#c4c4c4,#9a9a9a);font-family:'Roboto',sans-serif;font-weight:300;color:var(--ink);position:relative}
  .panel{position:absolute;background:var(--paper);box-shadow:0 4px 14px rgba(0,0,0,.28);overflow:hidden;z-index:0}

  /* Cover */
  .cover{left:245px;top:30px;width:280px;height:520px}
  .cover-brand{height:150px;display:flex;flex-direction:column;align-items:center;justify-content:center;font-weight:300;color:#1a1a1a;line-height:.95}
  .cover-brand .brand-name{font-size:52px;letter-spacing:-1px}
  .cover-brand .brand-line{font-size:40px}
  .cover-photo{position:absolute;left:0;top:150px;width:100%;height:370px;background:linear-gradient(#eef3f6 0%,#9a7a64 35%,#5d4a3f 55%,#77a23c 80%,#4f7f22 100%)}
  .cover-url{position:absolute;left:80px;bottom:20px;color:var(--white);font-weight:700;font-size:10px}

  /* Inside spread */
  .spread{left:40px;top:575px;width:484px;height:525px;background:linear-gradient(var(--paper) 45%,var(--paper-fade))}
  .inside{position:absolute;top:0;width:242px;height:100%}
  .inside.polo{left:0}
  .inside.knit{left:242px;border-left:1px solid #d8d8d8}
  .inside-visual{position:absolute;left:0;top:0;width:100%}
  .visual-polo{height:150px;background:linear-gradient(120deg,#4bb7dc 0%,#9b4d98 55%,#ecbcd6 100%)}
  .visual-knit{height:120px;background:linear-gradient(120deg,#222 0%,#4b5a8c 30%,#b4b4b4 45%,#e84b6e 65%,#f29b74 80%,#c93a3a 100%)}
  .band{position:absolute;left:0;top:120px;width:484px;height:22px;z-index:1;background:linear-gradient(90deg,var(--green) 0%,var(--green-light) 50%,var(--green) 100%)}
  .band-title{position:absolute;top:124px;z-index:2;font-family:'Michroma',sans-serif;font-weight:400;color:var(--white);font-size:11.5px;letter-spacing:1.5px;white-space:nowrap}
  .polo .band-title{left:14px}
  .knit .band-title{right:14px}
  .price-badge{position:absolute;left:92px;top:138px;width:62px;height:62px;z-index:3}
  .inside-body{position:absolute;left:12px;right:12px;font-size:5.6px;line-height:1.65;color:var(--ink-soft)}
  .polo .inside-body{top:208px}
  .knit .inside-body{top:152px}
  .intro{color:var(--green-text);font-size:7.6px;line-height:1.35;margin-bottom:12px;text-align:justify}
  .block{margin-bottom:8px}
  strong{color:var(--ink);font-weight:700}
  .swatches{display:grid;grid-template-columns:repeat(11,1fr);gap:2px 3.5px;margin:6px 0 8px}
  .swatch i{display:block;height:14px}
  .swatch span{display:block;font-size:2.4px;line-height:4px;white-space:nowrap;overflow:hidden}
  .cols{display:flex;gap:10px}
  .cols > div{flex:1}
  .size-row{display:flex;gap:8px}
  .size-row span:first-child{width:30px}

  /* Back */
  .back{left:560px;top:650px;width:290px;height:510px}
  .back-top{height:190px;padding:18px 22px 0}
  .back-title{font-family:'Michroma',sans-serif;font-weight:400;font-size:13px;letter-spacing:2px;color:#333;margin-bottom:8px}
  .back-text{font-size:6.8px;line-height:1.4;color:var(--ink-soft);margin-bottom:8px}
  .service-lists{display:flex;gap:22px;font-size:6.8px;color:var(--ink-soft);line-height:1.55}
  .service-lists ul{list-style:disc;padding-left:14px}
  .back-bottom{position:absolute;left:0;top:190px;width:100%;height:320px;background:var(--green);padding:16px 26px 0;color:var(--white)}
  .back-photo{height:118px;border:3px solid var(--white);background:linear-gradient(180deg,#f1f1f1 0%,#e8e8e8 30%,#3c8c3c 55%,#1e88c8 75%,#8b2b7a 100%)}
  .contact-lead{font-size:7.2px;margin:14px 0 8px}
  .contact-name{font-size:12px;font-weight:400;padding-left:12px}
  .contact-person{font-size:7.2px;padding-left:12px;margin-bottom:12px}
  .contact-lines{font-size:7.2px;line-height:1.55;padding-left:10px;color:var(--white);border-spacing:0}
  .contact-lines td:first-child{width:34px}
  .copyright{position:absolute;bottom:10px;left:0;width:100%;text-align:center;font-size:3.8px}
</style>
</head>
<body>

<section class="panel cover">
  <div class="cover-brand">
    <span class="brand-name">velmax</span>
    <span class="brand-line">artline</span>
  </div>
  <div class="cover-photo" role="img" aria-label="Foto: lachende Familie liegt auf einem Golfrasen am Loch">
    <span class="cover-url">www.velmax.de</span>
  </div>
</section>

<section class="panel spread">
  <article class="inside polo">
    <div class="inside-visual visual-polo" role="img" aria-label="Zeichnung: drei Polo-Shirts in Hellblau, Rosa und Lila"></div>
    <h2 class="band-title">POLO SHIRTS</h2>
    <svg class="price-badge" viewBox="0 0 100 100">
      <polygon fill="var(--red)" points="50,2 58,12 70,6 73,19 86,18 83,31 96,36 88,47 97,57 85,63 88,76 75,76 72,89 60,84 50,94 41,84 28,90 26,77 13,77 16,64 4,58 12,48 4,37 17,32 14,19 27,20 30,7 42,13"/>
      <text x="50" y="36" text-anchor="middle" fill="#fff" font-family="Roboto,sans-serif" font-size="11">ab</text>
      <text x="50" y="52" text-anchor="middle" fill="#fff" font-family="Roboto,sans-serif" font-weight="700" font-size="13">11,90 EUR</text>
      <text x="50" y="66" text-anchor="middle" fill="#fff" font-family="Roboto,sans-serif" font-size="9">zzgl. MwSt.</text>
    </svg>
    <div class="inside-body">
      <p class="intro">Großes Sortiment an kurzfristig verfügbaren POLO SHIRTS für Damen, Herren und Kinder aus Baumwolle, Mischqualität oder Funktions-Polyester.</p>
      <p><strong>Farben</strong>: Sehr große Farbauswahl für unsere Baumwoll-Polo-Shirts.<br>Aktuelle Farbkarte:</p>
      <div class="swatches">
        <div class="swatch"><i style="background:#e3201b"></i><span>tomato</span></div>
        <div class="swatch"><i style="background:#fafafa"></i><span>white</span></div>
        <div class="swatch"><i style="background:#d9d0bc"></i><span>beige</span></div>
        <div class="swatch"><i style="background:#f1e3a0"></i><span>light yellow</span></div>
        <div class="swatch"><i style="background:#f2e03c"></i><span>yellow</span></div>
        <div class="swatch"><i style="background:#c9d32f"></i><span>acid yellow</span></div>
        <div class="swatch"><i style="background:#17a04c"></i><span>green</span></div>
        <div class="swatch"><i style="background:#ee6420"></i><span>dark orange</span></div>
        <div class="swatch"><i style="background:#f4a01e"></i><span>gold yellow</span></div>
        <div class="swatch"><i style="background:#ef7a2a"></i><span>orange</span></div>
        <div class="swatch"><i style="background:#dc2121"></i><span>red</span></div>
        <div class="swatch"><i style="background:#e41d1d"></i><span>signal red</span></div>
        <div class="swatch"><i style="background:#4cb6e1"></i><span>sky blue</span></div>
        <div class="swatch"><i style="background:#edb6cf"></i><span>rose</span></div>
        <div class="swatch"><i style="background:#b6a7bf"></i><span>lila</span></div>
        <div class="swatch"><i style="background:#a2508f"></i><span>plum</span></div>
        <div class="swatch"><i style="background:#2e3c94"></i><span>royal</span></div>
        <div class="swatch"><i style="background:#2d2b6a"></i><span>dark royal</span></div>
        <div class="swatch"><i style="background:#3f2341"></i><span>aubergine</span></div>
        <div class="swatch"><i style="background:#9fb4d6"></i><span>light blue</span></div>
        <div class="swatch"><i style="background:#79c9d3"></i><span>mint</span></div>
        <div class="swatch"><i style="background:#12a1c9"></i><span>turquoise</span></div>
        <div class="swatch"><i style="background:#4d92d6"></i><span>opal</span></div>
        <div class="swatch"><i style="background:#aeaeb6"></i><span>grey heather</span></div>
        <div class="swatch"><i style="background:#9ccb7c"></i><span>lime green</span></div>
        <div class="swatch"><i style="background:#138a48"></i><span>dark green</span></div>
        <div class="swatch"><i style="background:#575757"></i><span>olive</span></div>
        <div class="swatch"><i style="background:#1d2148"></i><span>navy</span></div>
        <div class="swatch"><i style="background:#193852"></i><span>petrol</span></div>
        <div class="swatch"><i style="background:#6b1f35"></i><span>wine</span></div>
        <div class="swatch"><i style="background:#3b2614"></i><span>brown</span></div>
        <div class="swatch"><i style="background:#48474c"></i><span>graphite</span></div>
        <div class="swatch"><i style="background:#2a2522"></i><span>black</span></div>
      </div>
      <div class="cols block">
        <div>
          <strong>Größen</strong>
          <div class="size-row"><span>Herren</span><span>S – 3XL</span></div>
          <div class="size-row"><span>Damen</span><span>XS – XXL</span></div>
          <div class="size-row"><span>Kinder</span><span>98 – 164</span></div>
        </div>
        <div>
          <p><strong>Lieferzeit:</strong> ab Lager, kurzfristig</p>
          <p><strong>Bestickung:</strong> Veredelung möglich, Mindestmenge bei Bestickung 6 Teile</p>
        </div>
      </div>
      <p><strong>Preis:</strong> Polo Shirts ab € 11,90 zzgl. MwSt.<br>Nach Vorlage Ihres gewünschten Stickmotives mit Größenangabe unterbreiten wir Ihnen ein individuelles Angebot zum Stickpreis.</p>
    </div>
  </article>

  <article class="inside knit">
    <div class="inside-visual visual-knit" role="img" aria-label="Foto: aufgefächerte Strickpullover in vielen Farben"></div>
    <h2 class="band-title">STRICK PULLOVER</h2>
    <div class="inside-body">
      <p class="intro">Merino Strickpullover und -pullunder für Damen und Herren, in feinster Qualität, 100% australische Merinowolle, bei 40% maschinenwaschbar, Total Easy Care Ausrüstung, trocknergeeignet in verschiedenen klassischen und modischen Farben.</p>
      <div class="block">
        <strong>Größen</strong>
        <div class="size-row"><span>Herren</span><span>48 - 58</span></div>
        <div class="size-row"><span>Damen</span><span>36 - 48</span></div>
      </div>
      <p class="block"><strong>Info:</strong> Klassische Farben während der Saison ab Lager (je nach Saisonverlauf) solange der Vorrat reicht. Bei modischen Farben empfehlen wir Vororder.</p>
      <p class="block">Artikel 59939 velmax artline V-Pullunder Herren<br>Artikel 59940 velmax artline V-Pullover Herren<br>Artikel 81602 velmax artline V-Pullunder Damen<br>Artikel 81603 velmax artline V-Pullover Damen</p>
      <p class="block"><strong>Bestickung:</strong> Veredelung möglich,<br>Mindestmenge bei Bestickung: 6 Teile</p>
      <p class="block"><strong>Preis:</strong> Gerne unterbreiten wir Ihnen ein individuelles Angebot.</p>
      <p><strong>Referenzen:</strong> Mit unseren Qualitäten sind wir seit nunmehr 15 Jahren in zahlreichen Pro Shops vertreten: GC Talbrunn e.V., GC Wendelsau, GC Kirnfeld, GC Rosbach, GC Feldmoor uvm.</p>
    </div>
  </article>

  <div class="band"></div>
</section>

<section class="panel back">
  <div class="back-top">
    <h2 class="back-title">ÜBER UNS</h2>
    <p class="back-text">Pa dolorum necte adi dipsant que laborumqui rendigenis demquunt. At dis magnatem. Nonsed que laboratis molenectur, ne lhic tem eum fuga. Nam reicipsunti occus. Ebis re consequi alibus dolorentest, quatas aut volum fugia comnis reptatius, tem aliqui offici cus niandunti que nati</p>
    <div class="service-lists">
      <ul><li>Polo-Shirts</li><li>Strickpullover</li><li>V-Pullover</li><li>Bestickunsservice</li></ul>
      <ul style="list-style:none;padding-left:0">
        <li>Polo-Shirts</li><li>• &nbsp;Strickpullover</li><li>• &nbsp;V-Pullover</li><li>• &nbsp;Bestickunsservice</li>
      </ul>
    </div>
  </div>
  <div class="back-bottom">
    <div class="back-photo" role="img" aria-label="Foto: bunte Shirts auf weißen Kleiderbügeln an einer Stange"></div>
    <p class="contact-lead">Kontaktieren Sie uns:</p>
    <p class="contact-name">Velmax Handelsvertretung</p>
    <p class="contact-person">Marlitu Ebersold</p>
    <table class="contact-lines">
      <tr><td colspan="2">Kastanienallee 17</td></tr>
      <tr><td colspan="2">68199 Wernstadt</td></tr>
      <tr><td>Tel.:</td><td>+49 000 5550146</td></tr>
      <tr><td>Fax:</td><td>+49 000 5550147</td></tr>
      <tr><td>E-Mail:</td><td>kontakt@velmax.de</td></tr>
      <tr><td>Web:</td><td>www.velmax.de</td></tr>
    </table>
    <p class="copyright">© 2014 Velmax. Alle Rechte vorbehalten.</p>
  </div>
</section>

</body>
</html>
```